Window Cleaning Flyer targeting body corporates

Need a flyer for window cleaning targeting body corporate (approx A5 print size). It should be professional and match the logo attached.
We are looking to standout but not be to over the top for a window cleaning/services company.
We want to entice the receptionist or managers to call us because they see no good reason not to.

Industry/Entity Type

Window Cleaning

Font styles to use
Serif

Colors
0555a3
fbed22

Requirements
Must have
• Professional with a few of the photos attached included. Must include logo and the following contact details:
• Ph: 9413 6570
• email: admin@brightpaneworks.com.au
• PO Box 4726
• Marlowe Heights
• 3284
Nice to have
• Colours matching logo/ van print layout. Looking for more of a simplistic professional design.
Should not have
• Cartoon pictures, animated decorations or stock photos.

```html
<!DOCTYPE html>
<html lang="en">
<head>
<meta charset="utf-8">
<title>Bright Pane Window Cleaning – Body Corporate Flyer</title>
<link rel="stylesheet" href="https://fonts.googleapis.com/css2?family=Archivo:ital,wght@0,400;0,600;0,700;0,800;1,400;1,700&family=Roboto+Condensed:wght@700&display=swap">
<style>
  :root {
    --brand-blue: #0555a3;
    --deep-navy: #0b2a63;
    --brand-yellow: #fbed22;
    --paper: #f2f2f2;
    --ink: #222;
    --stage: #e6e6e6;
  }
  * { margin: 0; padding: 0; box-sizing: border-box; }
  html, body { width: 916px; height: 1200px; overflow: hidden; background: var(--stage); }
  body { position: relative; font-family: "Archivo", Arial, sans-serif; }

  .flyer {
    position: absolute;
    left: 49px; top: 20px;
    width: 874px; height: 1240px;
    transform: scale(0.9355);
    transform-origin: 0 0;
    background: var(--paper);
    overflow: hidden;
    box-shadow: 0 6px 18px rgba(0,0,0,.25);
  }
  .flyer-shapes { position: absolute; inset: 0; }

  .brand-name {
    position: absolute; right: 38px; top: 44px;
    color: var(--brand-yellow); font-weight: 800; text-align: right; text-transform: uppercase;
    line-height: 1;
  }
  .brand-name .line-main { display: block; font-size: 62px; letter-spacing: 1px; }
  .brand-name .line-sub { display: block; font-size: 23px; letter-spacing: 1.5px; margin-top: 14px; }

  .headline {
    position: absolute; left: 27px; top: 712px;
    color: var(--brand-blue); font-weight: 800; font-size: 28px; line-height: 40px;
    text-transform: uppercase; white-space: nowrap;
  }
  .headline .highlight { color: var(--brand-yellow); -webkit-text-stroke: 1px #c9b800; }
  .intro {
    position: absolute; left: 27px; top: 803px; width: 500px;
    color: var(--ink); font-size: 18px; line-height: 25px;
  }

  .specialty-banner {
    position: absolute; left: 0; top: 888px; width: 540px; height: 63px;
    background: linear-gradient(90deg, var(--brand-blue), var(--deep-navy));
    border-radius: 0 32px 32px 0;
    box-shadow: 0 3px 6px rgba(0,0,0,.3);
    color: #fff; font-family: "Roboto Condensed", "Arial Narrow", sans-serif; font-weight: 700; font-size: 25px;
    line-height: 63px; padding-left: 30px; text-transform: uppercase; white-space: nowrap; overflow: hidden;
  }

  .service-list { position: absolute; left: 30px; top: 980px; list-style: none; }
  .service { margin-bottom: 9px; }
  .service-name {
    display: flex; align-items: center; gap: 8px;
    color: var(--brand-blue); font-weight: 800; font-size: 21px; text-transform: uppercase;
  }
  .service-note { display: block; padding-left: 27px; font-size: 18px; color: #333; margin-top: 2px; }

  .pride-note {
    position: absolute; left: 0; width: 874px; top: 1137px; padding-left: 100px; text-align: center;
    color: var(--brand-blue); font-style: italic; font-size: 16.5px;
  }

  .contact-panel {
    position: absolute; left: 560px; top: 800px; width: 314px;
    text-align: center; color: #fff;
  }
  .contact-callout { font-style: italic; font-weight: 700; font-size: 22px; line-height: 27px; padding: 0 10px; }
  .contact-phone {
    display: flex; align-items: center; justify-content: center; gap: 16px;
    margin-top: 34px; color: var(--brand-yellow); font-weight: 800; font-size: 37px;
  }

  .footer-bar {
    position: absolute; left: 0; bottom: 0; width: 874px; height: 65px;
    background: linear-gradient(90deg, var(--brand-blue), var(--deep-navy));
    color: var(--brand-yellow); text-align: center; font-size: 21px; line-height: 65px; white-space: nowrap;
  }
</style>
</head>
<body>
<main class="flyer">
  <svg class="flyer-shapes" viewBox="0 0 874 1240" width="874" height="1240">
    <defs>
      <linearGradient id="navyFade" x1="0" y1="0" x2="1" y2="0">
        <stop offset="0" stop-color="#0555a3"/><stop offset="1" stop-color="#0b2a63"/>
      </linearGradient>
      <linearGradient id="panelFade" x1="0" y1="0" x2="1" y2="1">
        <stop offset="0" stop-color="#0a4fa0"/><stop offset="1" stop-color="#0b2a63"/>
      </linearGradient>
      <linearGradient id="photoTones" x1="0" y1="0" x2="1" y2="1">
        <stop offset="0" stop-color="#7d95ad"/><stop offset=".55" stop-color="#3b4c66"/><stop offset="1" stop-color="#a9bccb"/>
      </linearGradient>
      <linearGradient id="vanTones" x1="0" y1="0" x2="1" y2="1">
        <stop offset="0" stop-color="#6d8a5a"/><stop offset=".5" stop-color="#e9ecef"/><stop offset="1" stop-color="#8f959b"/>
      </linearGradient>
    </defs>
    <path d="M0 0 H874 V640 Q600 560 0 690 Z" fill="url(#navyFade)"/>
    <path d="M560 560 H874 V1030 H600 Q560 1030 560 990 Z" fill="url(#panelFade)"/>
    <path d="M0 108 Q430 60 874 310 V340 Q430 95 0 140 Z" fill="#fff"/>
    <path d="M0 112 Q430 66 874 316 V332 Q430 88 0 134 Z" fill="var(--brand-yellow)"/>
    <path d="M0 140 Q430 95 874 340 V560 Q600 545 0 655 Z" fill="url(#photoTones)" role="img" aria-label="Photo: two uniformed cleaners washing a car showroom's glass windows with extension poles"/>
    <path d="M0 655 Q600 545 874 600 V625 Q600 575 0 668 Z" fill="var(--brand-blue)"/>
    <path d="M0 665 Q600 572 874 622 V645 Q600 595 0 680 Z" fill="var(--brand-yellow)"/>
    <path d="M0 680 Q600 595 874 645 V650 Q600 602 0 686 Z" fill="#fff"/>
    <circle cx="720" cy="646" r="120" fill="#cfd4da"/>
    <circle cx="720" cy="646" r="114" fill="url(#vanTones)" role="img" aria-label="Photo: the company's white service van with its signage"/>
  </svg>

  <div class="brand-name"><span class="line-main">Bright Pane</span><span class="line-sub">Window Cleaning</span></div>

  <h1 class="headline">Let <span class="highlight">Bright Pane</span> take care of<br>your body corporate needs!</h1>
  <p class="intro">With over 15 years of experience we will ensure the job is completed to the highest standard everytime..</p>

  <div class="specialty-banner">Bright Pane specialises in body corporate</div>

  <ul class="service-list">
    <li class="service"><span class="service-name"><svg width="19" height="19" viewBox="0 0 20 20"><circle cx="10" cy="10" r="10" fill="var(--deep-navy)"/><path d="M8 5.5 L12.5 10 L8 14.5" stroke="#fff" stroke-width="2.6" fill="none"/></svg>Window cleaning</span></li>
    <li class="service"><span class="service-name"><svg width="19" height="19" viewBox="0 0 20 20"><circle cx="10" cy="10" r="10" fill="var(--deep-navy)"/><path d="M8 5.5 L12.5 10 L8 14.5" stroke="#fff" stroke-width="2.6" fill="none"/></svg>Gutter cleaning</span><span class="service-note">(using our ladder free gutter vacuum)</span></li>
    <li class="service"><span class="service-name"><svg width="19" height="19" viewBox="0 0 20 20"><circle cx="10" cy="10" r="10" fill="var(--deep-navy)"/><path d="M8 5.5 L12.5 10 L8 14.5" stroke="#fff" stroke-width="2.6" fill="none"/></svg>Pressure washing</span><span class="service-note">including moss treatment to prevent mould regrowth on concrete surface</span></li>
  </ul>

  <p class="pride-note">Bright Pane Window Cleaning take pride in being friendly and courteous to all residents.</p>

  <section class="contact-panel">
    <p class="contact-callout">Contact the Bright Pane Team for an easy, FREE quote today!</p>
    <p class="contact-phone">
      <svg width="48" height="48" viewBox="0 0 48 48" aria-hidden="true"><circle cx="24" cy="24" r="21.5" fill="none" stroke="var(--brand-yellow)" stroke-width="3"/><path d="M17 12 L21 12 L23 19 L20 21 Q22 27 27 29 L29 26 L36 28 L36 32 Q35 36 31 36 Q15 34 12 17 Q12 12 17 12 Z" fill="var(--brand-yellow)"/></svg>
      9413 6570
    </p>
  </section>

  <footer class="footer-bar">admin@brightpaneworks.com.au &nbsp;|&nbsp; PO Box 4726 Marlowe Heights 3284</footer>
</main>
</body>
</html>
```